Parcel Badge Inc. NEED DESIGNS FOR THE HOLIDAY STICKERS

We need 6 designs for the HOLIDAY SET of Parcel Badges. I have attached some imagery that we like as well as the flagship pack of stickers that were also designed by you AWESOME DESIGNERS!! You are not limited to this imagery, it is only to show you what style we like but remember, YOU ARE THE ARTIST! Each design needs to have a "TO: & FROM:" for people to write in their name and the recipients name. We need designs for the following occasions:

1. HALLOWEEN
2. HAPPY HOLIDAYS (THANKSGIVING, CHRISTMAS, WINTER, LEAVES)
3. ST. PATRICK'S DAY
4. "LET'S CELEBRATE" PATRIOTIC THEME (JULY 4TH, VETERANS DAY, MEMORIAL DAY COMBINED)
5. HAPPY NEW YEAR
6. SUMMER THEME GENERIC

***these 6 designs must fit on one of die cut shapes which are included in the brief***

**PLEASE SUBMIT YOUR IDEA FOR AS MANY DESIGNS AS YOU CAN (PREFERABLY ALL 6). WE NEED 6 DESIGNS SO IF 4 OF YOURS ARE GOOD AND 2 OF ANOTHERS ARE GOOD, YOU WOULD WIN 1ST AND THEY WOULD WIN 2ND.

Font styles to use
Serif
Sans Serif
Decorative
Script

Requirements
Must have
• - lines for "to" and "from"
• - must fit on a die cut shape (provided)
• - must be FUN and colorful!!
Nice to have
• color, imagery, fun!

```html
<!DOCTYPE html>
<html lang="en">
<head>
<meta charset="utf-8">
<title>Happy New Year 2017 Gift Sticker</title>
<link rel="stylesheet" href="https://fonts.googleapis.com/css2?family=Chewy&family=Great+Vibes&display=swap">
<style>
  :root {
    --backdrop: #999999;
    --label-fill: #f4fbd6;
    --label-edge: #ffffff;
    --ink-green: #2e9a1f;
    --outline-dark: #0b0f2a;
    --sky-deep: #0a1033;
    --sky-mid: #1a3a8a;
    --glass-dark: #14121c;
    --glass-light: #3a3848;
  }
  html, body {
    margin: 0;
    padding: 0;
    width: 1200px;
    height: 1200px;
    overflow: hidden;
    background: var(--backdrop);
  }
  .sticker {
    display: block;
    width: 1200px;
    height: 1200px;
  }
  .title-word {
    font-family: "Chewy", "Comic Sans MS", cursive;
    text-anchor: middle;
    paint-order: stroke fill;
    stroke-linejoin: round;
  }
  .title-word--outer {
    fill: none;
    stroke: var(--label-edge);
    stroke-width: 26px;
  }
  .title-word--inner {
    stroke: var(--outline-dark);
    stroke-width: 12px;
  }
  .field-label {
    font-family: "Great Vibes", "Brush Script MT", cursive;
    font-size: 40px;
    font-weight: 700;
    fill: var(--ink-green);
  }
  .field-line {
    stroke: var(--ink-green);
    stroke-width: 3;
    stroke-dasharray: 2 7;
    stroke-linecap: round;
  }
</style>
</head>
<body>
<svg class="sticker" viewBox="0 0 1200 1200" xmlns="http://www.w3.org/2000/svg">
  <defs>
    <linearGradient id="grad-happy" x1="0" y1="0" x2="0" y2="1">
      <stop offset="0" stop-color="#ff3a2a"/>
      <stop offset="1" stop-color="#b80000"/>
    </linearGradient>
    <linearGradient id="grad-newyear" x1="0" y1="0" x2="0" y2="1">
      <stop offset="0" stop-color="#6ffcff"/>
      <stop offset="1" stop-color="#1aa6e8"/>
    </linearGradient>
    <linearGradient id="grad-year" x1="0" y1="0" x2="0" y2="1">
      <stop offset="0" stop-color="#ff3cf2"/>
      <stop offset="1" stop-color="#7a1a8a"/>
    </linearGradient>
    <radialGradient id="grad-fireworks" cx="0.5" cy="0.5" r="0.6">
      <stop offset="0" stop-color="var(--sky-mid)"/>
      <stop offset="1" stop-color="var(--sky-deep)"/>
    </radialGradient>
    <linearGradient id="grad-bottle" x1="0" y1="0" x2="1" y2="0">
      <stop offset="0" stop-color="var(--glass-dark)"/>
      <stop offset="0.5" stop-color="var(--glass-light)"/>
      <stop offset="1" stop-color="var(--glass-dark)"/>
    </linearGradient>
  </defs>

  <!-- label body -->
  <ellipse class="label-body" cx="608" cy="738" rx="362" ry="222"
           fill="var(--label-fill)" stroke="var(--label-edge)" stroke-width="7"/>

  <!-- bottles -->
  <g class="bottle bottle--left" role="img" aria-label="Wine bottle photograph tilted left">
    <rect x="316" y="250" width="80" height="260" rx="26"
          transform="rotate(-30 356 380)" fill="url(#grad-bottle)"
          stroke="var(--label-edge)" stroke-width="6"/>
  </g>
  <g class="bottle bottle--right" role="img" aria-label="Wine bottle photograph tilted right">
    <rect x="810" y="252" width="80" height="250" rx="26"
          transform="rotate(30 850 377)" fill="url(#grad-bottle)"
          stroke="var(--label-edge)" stroke-width="6"/>
  </g>

  <!-- fireworks backdrop -->
  <g class="fireworks" role="img" aria-label="Night sky with colourful fireworks">
    <path d="M430 372 Q600 340 790 372 Q800 430 780 470 Q860 500 858 560 Q840 590 760 600 Q740 680 610 688 Q500 680 490 600 Q360 590 358 550 Q370 500 420 480 Q410 420 430 372 Z"
          fill="url(#grad-fireworks)" stroke="var(--label-edge)" stroke-width="6"/>
  </g>

  <!-- title -->
  <g class="title">
    <text class="title-word title-word--outer" x="606" y="444" font-size="104">Happy</text>
    <text class="title-word title-word--inner" x="606" y="444" font-size="104" fill="url(#grad-happy)">Happy</text>

    <text class="title-word title-word--outer" x="608" y="566" font-size="102">New Year</text>
    <text class="title-word title-word--inner" x="608" y="566" font-size="102" fill="url(#grad-newyear)">New Year</text>

    <text class="title-word title-word--outer" x="610" y="668" font-size="94">2017</text>
    <text class="title-word title-word--inner" x="610" y="668" font-size="94" fill="url(#grad-year)">2017</text>
  </g>

  <!-- to / from fields -->
  <g class="fields">
    <text class="field-label" x="334" y="774">To</text>
    <line class="field-line" x1="382" y1="770" x2="880" y2="770"/>
    <text class="field-label" x="334" y="870">From</text>
    <line class="field-line" x1="426" y1="866" x2="880" y2="866"/>
  </g>
</svg>
</body>
</html>
```